Optimising your students' achievement in PLQ English

The flyer is for an audience of English teachers in NSW, who are teaching PLQ English. We need a flyer that provides clear information about the services we can offer in terms of advice and professional learning for English teachers.
We are leading experts in this field and this is the first time we are offering tailored professional learning for individual schools and their English staff.
Attached is a document that provides details of the proposed content and inclusions (logos) for the flyer.

```html
<!DOCTYPE html>
<html lang="en">
<head>
<meta charset="utf-8">
<title>Optimising your students' achievement in PLQ English</title>
<link rel="stylesheet" href="https://fonts.googleapis.com/css2?family=Archivo+Black&family=Tinos:wght@400;700&display=swap">
<style>
  :root {
    --sky: #8fd3ec;
    --sky-soft: #9ad8ef;
    --slate: #4f7384;
    --ink: #1b2c48;
    --divider: #6fa9c2;
    --photo: #595959;
    --band: #b9e4f4;
    --mark: #1b2c48;
  }
  * { margin: 0; padding: 0; box-sizing: border-box; }
  html, body { width: 1200px; height: 850px; overflow: hidden; background: var(--sky); }
  .flyer {
    position: relative; width: 1200px; height: 850px; overflow: hidden;
    background: linear-gradient(180deg, var(--sky-soft) 0%, var(--sky) 100%);
    font-family: "Tinos", "Times New Roman", serif; color: var(--ink);
  }
  .panel-divider { position: absolute; top: 0; width: 1px; height: 850px; background: var(--divider); }

  .quote {
    position: absolute; font-family: "Archivo Black", "Arial Black", sans-serif;
    color: var(--slate); font-size: 31px; line-height: 36px; letter-spacing: 0.3px;
  }
  .quote .author { display: block; margin-top: 36px; }

  .body-text { position: absolute; font-size: 18px; line-height: 24px; }
  .bullet-list { list-style: none; position: absolute; font-size: 18px; line-height: 24px; }
  .bullet-list > li { position: relative; padding-left: 34px; margin-bottom: 24px; }
  .bullet-list > li::before { content: "•"; position: absolute; left: 20px; top: 0; }

  .program-list { list-style: none; position: absolute; font-size: 18px; line-height: 24px; }
  .program-list li { position: absolute; white-space: nowrap; }

  .consultants-band { position: absolute; left: 803px; top: 44px; }
  .consultants-title {
    position: absolute; left: 822px; top: 58px;
    font-family: "Archivo Black", "Arial Black", sans-serif; font-size: 20px; line-height: 28px; color: var(--ink);
  }
  .photo {
    position: absolute; left: 822px; width: 122px; height: 150px; background: var(--photo);
    color: #fff; font-size: 15px; display: flex; align-items: center; justify-content: center;
  }
  .affiliation { position: absolute; left: 822px; display: flex; align-items: center; gap: 8px;
    font-size: 17px; color: var(--ink); }
  .affiliation .mark { width: 40px; height: 40px; background: var(--mark); }
  .bio { position: absolute; left: 822px; width: 370px; font-size: 16px; line-height: 26.5px; white-space: nowrap; }
  .bio .name { font-weight: 700; font-size: 17px; }
</style>
</head>
<body>
<div class="flyer">
  <div class="panel-divider" style="left:400px"></div>
  <div class="panel-divider" style="left:800px"></div>

  <blockquote class="quote" style="left:28px;top:66px;">
    “ Man's mind,<br>once stretched by<br>a new idea, never<br>regains its<br>original<br>dimensions.”
    <span class="author">- Edmund Harrow<br>Wells</span>
  </blockquote>

  <p class="body-text" style="left:20px;top:463px;">We will work with you and your staff to:</p>
  <ul class="bullet-list" style="left:20px;top:511px;width:380px;">
    <li>Develop and/or provide advice on all<br>aspects of Stage 6 English programs for<br>optimal student engagement and learning<br>outcomes</li>
    <li>Provide intensive professional learning<br>to assist Stage 6 English teachers in<br>raising students’ achievement in PLQ<br>English examinations (one-off<br>professional learning days tailored to<br>your needs, and/or sustained<br>collaboration with your staff)</li>
  </ul>

  <ul class="bullet-list" style="left:420px;top:34px;width:380px;">
    <li>Provide targeted programs in:</li>
  </ul>
  <ol class="program-list" style="left:446px;top:82px;">
    <li style="top:0;">i.&nbsp; Preparing your students for PLQ<br>&nbsp;&nbsp;&nbsp;&nbsp;English examinations: what they need<br>&nbsp;&nbsp;&nbsp;&nbsp;to know to succeed in English<br>&nbsp;&nbsp;&nbsp;&nbsp;examinations</li>
    <li style="top:120px;">ii. Teaching and learning resources<br>&nbsp;&nbsp;&nbsp;&nbsp;specifically focused on building<br>&nbsp;&nbsp;&nbsp;&nbsp;examination technique and<br>&nbsp;&nbsp;&nbsp;&nbsp;confidence</li>
    <li style="top:240px;">iii. Successfully planning, programming,<br>&nbsp;&nbsp;&nbsp;&nbsp;&nbsp;&nbsp;teaching and resourcing Stage 6<br>&nbsp;&nbsp;&nbsp;&nbsp;&nbsp;&nbsp;English</li>
    <li style="top:336px;">iv. Research-based strategies and the<br>&nbsp;&nbsp;&nbsp;&nbsp;&nbsp;most effective pedagogy for<br>&nbsp;&nbsp;&nbsp;&nbsp;&nbsp;developing students’ writing abilities<br>&nbsp;&nbsp;&nbsp;&nbsp;&nbsp;in PLQ English examinations</li>
  </ol>

  <blockquote class="quote" style="left:433px;top:556px;">
    “ It's what you<br>learn after you<br>know it all that<br>counts.”
    <span class="author">- Martin J Avery</span>
  </blockquote>

  <svg class="consultants-band" width="310" height="58" viewBox="0 0 310 58" role="img" aria-label="Heading band">
    <polygon points="0,0 290,0 310,29 290,58 0,58" fill="var(--band)"/>
  </svg>
  <h2 class="consultants-title">Consultants</h2>

  <div class="photo" style="top:119px;" role="img" aria-label="Portrait photograph of Helena Marlow">Photograph</div>
  <div class="affiliation" style="top:283px;"><span class="mark"></span>Westbrook University</div>
  <div class="bio" style="top:327px;">
    <div class="name">Associate Professor Helena Marlow</div>
    <div>Westbrook University</div>
    <div>Chief Examiner, PLQ English (Standard and<br>Advanced, 2006-2011)</div>
  </div>

  <div class="photo" style="top:447px;" role="img" aria-label="Portrait photograph of Owen Tasker">Photograph</div>
  <div class="affiliation" style="top:623px;"><span class="mark"></span>Northgate Christian University</div>
  <div class="bio" style="top:674px;">
    <div class="name">Dr Owen Tasker</div>
    <div>Northgate Christian University</div>
    <div>Former Inspector, English at the Regional<br>Council of Curriculum, Teaching and<br>Educational Standards</div>
  </div>
</div>
</body>
</html>
```